Autohaus sucht Visitenkarten
Zielgruppe
Verkauf und Reparatur von PKW
Zielgruppe ist jeder Autofahrer/in
Aufgabenstellung
Erstellen eines Visitenkartendesigns mit stilisiertem Auto als Logo, eher modern gestaltet, ohne Schnörkel, zweifarbig, Anthrazit sollte im Logo enthalten sein.

```html
<!DOCTYPE html>
<html lang="de">
<head>
<meta charset="utf-8">
<title>RSW-Fahrzeuge – Visitenkarte</title>
<link rel="stylesheet" href="https://fonts.googleapis.com/css2?family=Lato:wght@400;700;900&display=swap">
<style>
  :root {
    --stage: #e4e6e7;
    --anthracite: #2a2c2e;
    --anthracite-light: #35383a;
    --accent-green: #5fd62c;
    --silver-light: #f4f4f4;
    --silver-mid: #b9bcbe;
    --silver-dark: #7d8083;
    --text-light: #f1f1f1;
    --logo-grey: #d6d8d9;
  }
  * { box-sizing: border-box; margin: 0; padding: 0; }
  html, body {
    width: 1200px; height: 960px; overflow: hidden;
    background: var(--stage);
    font-family: "Lato", Arial, sans-serif;
  }
  .sheet {
    width: 1200px; height: 960px;
    display: flex; flex-direction: column; align-items: center; justify-content: center;
    gap: 40px;
  }
  .card {
    position: relative;
    width: 640px; height: 414px;
    background: radial-gradient(ellipse at 35% 40%, var(--anthracite-light), var(--anthracite) 70%);
    box-shadow: 0 10px 28px rgba(0,0,0,0.25);
    overflow: hidden;
  }
  /* Wordmark */
  .wordmark { position: absolute; }
  .wordmark__name {
    font-weight: 900; font-size: 46px; color: var(--logo-grey);
    letter-spacing: 0.5px; line-height: 1;
  }
  .wordmark__tagline {
    margin-top: 6px;
    font-weight: 400; font-size: 17px; color: var(--accent-green);
    letter-spacing: 1.6px;
  }
  /* Front */
  .card--front .wordmark { left: 48px; top: 192px; }
  .contact {
    position: absolute; right: 78px; top: 82px;
    text-align: right; color: var(--text-light);
  }
  .contact__person { font-size: 23px; color: var(--accent-green); margin-bottom: 22px; }
  .contact__address { font-size: 15px; line-height: 1.45; }
  .contact__lines { margin-top: 22px; font-size: 15px; line-height: 1.6; }
  .contact__line { display: flex; justify-content: flex-end; align-items: center; gap: 7px; }
  .contact__line svg { width: 12px; height: 12px; }
  .edge-bar {
    position: absolute; right: 50px; top: 80px;
    width: 11px; height: 168px;
    background: linear-gradient(90deg, var(--silver-dark), var(--silver-light) 55%, var(--silver-mid));
    border-right: 3px solid var(--accent-green);
  }
  /* Back */
  .card--back .wordmark { left: 0; right: 0; top: 150px; text-align: center; }
  .card--back .wordmark__name { font-size: 52px; }
  .card--back .wordmark__tagline { font-size: 18px; }
  .back__email {
    position: absolute; left: 0; right: 0; top: 298px;
    text-align: center; color: var(--text-light); font-size: 16px; letter-spacing: 1px;
  }
  .side-curve { position: absolute; top: 0; height: 414px; width: 40px; }
  .side-curve--left { left: 0; }
  .side-curve--right { right: 0; transform: scaleX(-1); }
</style>
</head>
<body>
<main class="sheet">

  <section class="card card--front" aria-label="Vorderseite">
    <div class="wordmark">
      <div class="wordmark__name">RSW-Fahrzeuge</div>
      <div class="wordmark__tagline">Verkauf und Reparatur von PKW</div>
    </div>
    <div class="contact">
      <div class="contact__person">Jonas Wertacher</div>
      <div class="contact__address">
        RSW-Fahrzeuge<br>Lindenstraße 12<br>89312 Günzburg
      </div>
      <div class="contact__lines">
        <div class="contact__line">08 221 / 4712 305
          <svg viewBox="0 0 12 12" aria-hidden="true"><path d="M3 1.5 L4.6 3.8 L3.6 5 Q4.6 7.2 7 8.4 L8.2 7.4 L10.5 9 L9.4 10.6 Q4 10 1.4 2.6 Z" fill="var(--accent-green)"/></svg>
        </div>
        <div class="contact__line">RSW-Fahrzeuge@mailpost.de
          <svg viewBox="0 0 12 12" aria-hidden="true"><rect x="1" y="2.5" width="10" height="7" rx="1" fill="var(--accent-green)"/><path d="M1.5 3 L6 6.6 L10.5 3" stroke="var(--anthracite)" stroke-width="1" fill="none"/></svg>
        </div>
      </div>
    </div>
    <div class="edge-bar"></div>
  </section>

  <section class="card card--back" aria-label="Rückseite">
    <svg class="side-curve side-curve--left" viewBox="0 0 40 414" preserveAspectRatio="none" aria-hidden="true">
      <defs>
        <linearGradient id="silverEdge" x1="0" x2="1" y1="0" y2="0">
          <stop offset="0" stop-color="#f4f4f4"/>
          <stop offset="0.6" stop-color="#b9bcbe"/>
          <stop offset="1" stop-color="#7d8083"/>
        </linearGradient>
      </defs>
      <path d="M0 0 L4 0 Q34 207 4 414 L0 414 Z" fill="url(#silverEdge)"/>
      <path d="M4 0 Q34 207 4 414" stroke="var(--accent-green)" stroke-width="2" fill="none"/>
    </svg>
    <svg class="side-curve side-curve--right" viewBox="0 0 40 414" preserveAspectRatio="none" aria-hidden="true">
      <path d="M0 0 L4 0 Q34 207 4 414 L0 414 Z" fill="url(#silverEdge)"/>
      <path d="M4 0 Q34 207 4 414" stroke="var(--accent-green)" stroke-width="2" fill="none"/>
    </svg>
    <div class="wordmark">
      <div class="wordmark__name">RSW-Fahrzeuge</div>
      <div class="wordmark__tagline">Verkauf und Reparatur von PKW</div>
    </div>
    <div class="back__email">RSW-Fahrzeuge@mailpost.de</div>
  </section>

</main>
</body>
</html>
```